Business Card design for an International Import Export House

We need a Business Card design for our import export business. We trade in Minerals, Metals, Rice, Sugar, Steel etc.. The design should be minimalistic. It may or may not contain the physical address. In case you want to include the physical address - 418 Verandah Heights, Marlow Sector 9, Gurgaon, Haryana, India, 122009.

Target Market(s)

Steel Mills or Steel Plants, Factories, Mining businesses, Industrial houses, Government Agencies

Industry/Entity Type

Importer

Contact Information for Business Card

Business Name - Qirvale Overseas

Font styles to use
Other font styles liked:
• montserrat

Requirements
Must have
• Ravi Kandola - President
• www.qirvaleoverseas.com
• ravi@qirvaleoverseas.com
• +91-987-654-3217
Nice to have
• worldwide suppliers of ores

```html
<!DOCTYPE html>
<html lang="en">
<head>
<meta charset="utf-8">
<title>Qirvale Overseas – Business Card</title>
<link href="https://fonts.googleapis.com/css2?family=Montserrat:wght@300;400;500;600;700&display=swap" rel="stylesheet">
<style>
  :root {
    --backdrop: #e9ebec;
    --card: #ffffff;
    --teal: #3c93aa;
    --teal-light: #58b2c6;
    --teal-deep: #2a7690;
    --ink: #2c2f33;
    --muted: #8b9196;
    --on-teal: #eaf6f9;
  }
  * { box-sizing: border-box; margin: 0; padding: 0; }
  html, body {
    width: 1200px; height: 1000px; overflow: hidden;
    background: var(--backdrop);
    font-family: "Montserrat", sans-serif;
  }
  .stage {
    width: 1200px; height: 1000px;
    display: flex; align-items: center; justify-content: center; gap: 100px;
  }
  .card {
    width: 360px; height: 620px;
    background: var(--card);
    display: flex; flex-direction: column;
    box-shadow: 0 10px 30px rgba(0,0,0,0.15);
  }
  .band {
    background: linear-gradient(120deg, var(--teal-deep), var(--teal) 55%, var(--teal-light));
    color: var(--on-teal);
    display: flex; align-items: center; justify-content: center;
    text-align: center;
  }

  /* Front */
  .front .tagline-band { height: 90px; }
  .tagline { font-size: 15px; font-weight: 600; letter-spacing: 1px; text-transform: uppercase; white-space: nowrap; }
  .front .brand-area { flex: 1; display: flex; flex-direction: column; align-items: center; justify-content: center; gap: 26px; }
  .brand-dot { width: 120px; height: 120px; border-radius: 50%; background: var(--teal-light); }
  .brand-name { font-size: 28px; font-weight: 700; color: var(--ink); text-transform: uppercase; letter-spacing: 0.5px; white-space: nowrap; }
  .front .web-band { height: 150px; }
  .web { font-size: 19px; font-weight: 400; letter-spacing: 0.5px; white-space: nowrap; }

  /* Back */
  .back .brand-area { height: 230px; display: flex; flex-direction: column; align-items: center; justify-content: center; gap: 16px; }
  .back .brand-dot { width: 72px; height: 72px; }
  .back .brand-name { font-size: 19px; }
  .back .person-band { height: 170px; flex-direction: column; gap: 6px; }
  .person-name { font-size: 22px; font-weight: 300; letter-spacing: 1px; text-transform: uppercase; }
  .person-role { font-size: 18px; font-weight: 500; }
  .contacts { flex: 1; display: flex; flex-direction: column; justify-content: flex-end; gap: 16px; padding: 0 30px 40px; list-style: none; }
  .contact { display: flex; align-items: center; gap: 14px; font-size: 16px; color: var(--muted); white-space: nowrap; }
  .contact svg { width: 16px; height: 16px; flex: none; }
</style>
</head>
<body>
<main class="stage">
  <section class="card front" aria-label="Card front">
    <div class="band tagline-band"><p class="tagline">Worldwide suppliers of ores</p></div>
    <div class="brand-area">
      <span class="brand-dot"></span>
      <p class="brand-name">Qirvale Overseas</p>
    </div>
    <div class="band web-band"><p class="web">www.qirvaleoverseas.com</p></div>
  </section>

  <section class="card back" aria-label="Card back">
    <div class="brand-area">
      <span class="brand-dot"></span>
      <p class="brand-name">Qirvale Overseas</p>
    </div>
    <div class="band person-band">
      <p class="person-name">Ravi Kandola</p>
      <p class="person-role">President</p>
    </div>
    <ul class="contacts">
      <li class="contact">
        <svg viewBox="0 0 16 16" aria-hidden="true"><rect x="4" y="1" width="8" height="14" rx="1.5" fill="none" stroke="var(--teal-light)" stroke-width="1.4"/><circle cx="8" cy="12.5" r="0.9" fill="var(--teal-light)"/></svg>
        <span>+91-987-654-3217</span>
      </li>
      <li class="contact">
        <svg viewBox="0 0 16 16" aria-hidden="true"><rect x="1" y="3" width="14" height="10" rx="1" fill="var(--teal-light)"/><path d="M1.5 3.8 8 9l6.5-5.2" fill="none" stroke="#fff" stroke-width="1.2"/></svg>
        <span>ravi@qirvaleoverseas.com</span>
      </li>
      <li class="contact">
        <svg viewBox="0 0 16 16" aria-hidden="true"><circle cx="8" cy="8" r="7" fill="var(--teal-light)"/><path d="M1 8h14M8 1c-3 3.5-3 10.5 0 14M8 1c3 3.5 3 10.5 0 14" fill="none" stroke="#fff" stroke-width="1"/></svg>
        <span>www.qirvaleoverseas.com</span>
      </li>
    </ul>
  </section>
</main>
</body>
</html>
```